Managed Service Provider need new business cards

We are a small Maanged Service Provider of IT Services and need a new fresh design for our business cards. We want something impossible, fun and professional :)
Our services has a large range, but we are always fun and make sure our customers both get their issue sorted and also feel like they are "catching up with an old friend".
All our cards in the past has always been all black, with red and we need something fresher.
The back of card, we would like just a small list of what we do i think, but if someone has a better idea, please do something cool with the back of the card:
Managed IT Services
Productivity Solutions
Data Backup and Recovery
IT System Maintenance
Managed IT Security
More details can be found on our website qvtechworks.com.au
Industry/Entity Type
It Company
Contact Information for Business Card
Name: Simon Trelawny
Title: Director
Phone: 03 6158 4932
Mobile: 0417 582 139
Email: simon@qvtechworks.com.au
Web: www.qvtechworks.com.au
Look and feel
Each slider illustrates characteristics of the customer's brand and the style your logo design should communicate.

```html
<!DOCTYPE html>
<html lang="en">
<head>
<meta charset="utf-8">
<title>QV Techworks – Business Card</title>
<link href="https://fonts.googleapis.com/css2?family=Jost:wght@400;500;600;700&display=swap" rel="stylesheet">
<style>
  :root {
    --bg: #f1f1f1;
    --charcoal: #3a3a3a;
    --paper: #f7f7f7;
    --red: #e31b23;
    --ink: #333333;
    --muted: #6e6e6e;
    --light: #d6d6d6;
    --white: #ffffff;
  }
  * { margin: 0; padding: 0; box-sizing: border-box; }
  html, body {
    width: 1200px; height: 1200px; overflow: hidden;
    background: var(--bg);
    font-family: "Jost", sans-serif;
  }
  .canvas { position: relative; width: 1200px; height: 1200px; }

  .card { position: absolute; overflow: hidden; }

  /* Front */
  .card-front {
    left: 208px; top: 109px; width: 767px; height: 447px;
    background: var(--charcoal);
  }
  .front-brand {
    position: absolute; left: 0; right: 0; top: 178px;
    text-align: center;
    color: var(--red); font-weight: 700; font-size: 64px;
    letter-spacing: 2px; line-height: 1;
  }
  .front-web {
    position: absolute; left: 0; right: 0; top: 414px;
    text-align: center;
    color: var(--white); font-size: 11px; font-weight: 500;
    letter-spacing: 10.5px;
  }

  /* Back */
  .card-back {
    left: 208px; top: 620px; width: 769px; height: 446px;
    background: var(--paper);
  }
  .back-split { position: absolute; inset: 0; }

  .person { position: absolute; left: 39px; top: 34px; }
  .person-name {
    font-size: 21px; font-weight: 600; letter-spacing: 1px;
    color: var(--ink); line-height: 1;
  }
  .person-name .surname { color: var(--red); }
  .person-title {
    margin-top: 6px; font-size: 11px; color: var(--muted);
    letter-spacing: 0.3px;
  }

  .contacts { position: absolute; left: 39px; top: 120px; list-style: none; }
  .contacts li { display: flex; align-items: baseline; color: var(--muted); }
  .contacts .label {
    width: 16px; color: var(--red); font-weight: 600; font-size: 11px;
  }
  .contacts .phone { font-size: 15px; height: 24px; letter-spacing: 0.3px; }
  .contacts .small { font-size: 12px; height: 23px; }

  .back-brand {
    position: absolute; left: 282px; top: 196px;
    color: var(--red); font-weight: 700; font-size: 26px;
    letter-spacing: 1px; line-height: 1;
  }

  .services { position: absolute; left: 485px; top: 252px; }
  .services-title {
    font-size: 13px; font-weight: 700; letter-spacing: 1.5px;
    color: var(--white);
  }
  .services-title .accent { color: var(--red); }
  .services-list { list-style: none; margin-top: 18px; }
  .services-list li {
    font-size: 15px; letter-spacing: 2px; color: var(--light);
    height: 27.5px;
  }
  .edge-bar {
    position: absolute; right: 0; top: 260px; width: 4px; height: 186px;
    background: var(--red);
  }
</style>
</head>
<body>
<main class="canvas">

  <section class="card card-front">
    <div class="front-brand">QV TECHWORKS</div>
    <div class="front-web">www.qvtechworks.com.au</div>
  </section>

  <section class="card card-back">
    <svg class="back-split" width="769" height="446" viewBox="0 0 769 446" aria-hidden="true">
      <polygon points="0,446 769,0 769,446" fill="var(--charcoal)"/>
    </svg>

    <div class="person">
      <div class="person-name">SIMON <span class="surname">TRELAWNY</span></div>
      <div class="person-title">Managing Director</div>
    </div>

    <ul class="contacts">
      <li class="phone"><span class="label">T</span>: 03 6158 4932 &nbsp;, 0417 582 139</li>
      <li class="small"><span class="label">E</span>: simon@qvtechworks.com.au</li>
      <li class="small"><span class="label">W</span>: www.qvtechworks.com.au</li>
    </ul>

    <div class="back-brand">QV TECHWORKS</div>

    <div class="services">
      <div class="services-title">Our <span class="accent">Services</span></div>
      <ul class="services-list">
        <li>- Managed IT Services</li>
        <li>- Productivity Solutions</li>
        <li>- Data Backup and Recovery</li>
        <li>- IT System Maintenance</li>
        <li>- Managed IT Security</li>
      </ul>
    </div>

    <div class="edge-bar"></div>
  </section>

</main>
</body>
</html>
```